Maple Ridge Wellness Website Re-design

I need a re-design for an existing website www.MapleRidgeWellness-example.com - would like it in WORDPRESS, responsive including a FB page. New design and images are important to my client. I have a webdesign company but I have lost my graphic artist. Right now the site is hosted at Sitrova but client has hosting with Nexahost. All site designs and changes will be handled by me, Daniel Pruett

Number of Pages Required

5+ page

Font styles to use
Sans Serif

Requirements
Must have
• This is a website re-design that is a responsive WP template with new images and new home page look. All other pages are the same layout with new images to match the content. This should not be that hard for a website designer / graphic artist. Thank you, Daniel www.MapleRidgeWellness-example.com

```html
<!DOCTYPE html>
<html lang="en">
<head>
<meta charset="utf-8">
<title>Maple Ridge Wellness</title>
<link rel="stylesheet" href="https://fonts.googleapis.com/css2?family=Open+Sans:wght@400;600;700&family=Raleway:wght@400;500;600&display=swap">
<style>
  :root {
    --teal: #22d3c5;
    --teal-pale: #c9f4f0;
    --navy: #1d1a4f;
    --orange: #f7881f;
    --text: #222222;
    --band-dark: #141c26;
    --footer: #2b2b2b;
    --grey-section: #f1f1f1;
    --line: #d8d8d8;
    --page-bg: #ffffff;
  }
  * { box-sizing: border-box; margin: 0; padding: 0; }
  html, body { width: 1200px; height: 1000px; overflow: hidden; background: var(--page-bg); }
  body { font-family: "Open Sans", Arial, sans-serif; color: var(--text); position: relative; }

  .page {
    position: absolute; left: 267px; top: 5px; width: 693px; height: 992px;
    background: #fff; box-shadow: 3px 3px 4px rgba(0,0,0,.45);
    overflow: hidden;
  }

  /* header */
  .site-header { position: absolute; left: 0; top: 0; width: 100%; height: 49px; border-bottom: 1px solid var(--line); }
  .brand { position: absolute; left: 56px; top: 15px; display: flex; align-items: center; gap: 6px; }
  .brand-dot { width: 14px; height: 14px; border-radius: 50%; background: var(--teal); }
  .brand-name { font-family: "Open Sans", sans-serif; font-weight: 700; font-size: 15px; color: var(--navy); }
  .main-nav { position: absolute; left: 0; top: 0; width: 100%; height: 49px; }
  .main-nav a { position: absolute; top: 0; height: 49px; line-height: 46px; font-size: 10px; color: #111; text-decoration: none; white-space: nowrap; }
  .main-nav a.active { left: 302px; width: 53px; text-align: center; background: var(--teal); color: #fff; }
  .main-nav a.active::after { content: ""; position: absolute; left: 50%; bottom: 0; margin-left: -4px; border: 4px solid transparent; border-bottom-color: #fff; }
  .main-nav .n-programs { left: 366px; }
  .main-nav .n-admissions { left: 434px; }
  .main-nav .n-about { left: 508px; }
  .main-nav .n-contact { left: 572px; }

  /* hero */
  .hero { position: absolute; left: 0; top: 49px; width: 100%; height: 262px;
    background: linear-gradient(90deg, #eef1f2 0%, #ffffff 25%, #ffffff 60%, #f4f5f6 100%); }
  .hero-photo { position: absolute; right: 0; top: 0; width: 370px; height: 262px;
    background: radial-gradient(ellipse at 45% 35%, #eccfbf 0%, #d9c0b3 22%, #f2f0ef 55%, #e9ecee 100%); }
  .hero-title { position: absolute; left: 54px; top: 86px; font-family: "Raleway", sans-serif; line-height: 1; }
  .hero-title .line-1 { display: block; font-size: 25px; color: var(--navy); font-weight: 400; letter-spacing: .5px; }
  .hero-title .line-2 { display: block; font-size: 39px; color: var(--orange); font-weight: 400; margin-top: 8px; letter-spacing: .5px; }

  /* services */
  .services { position: absolute; left: 0; top: 340px; width: 100%; height: 180px; }
  .service { position: absolute; top: 0; width: 140px; height: 180px; text-align: center; }
  .service-icon { width: 78px; height: 78px; border-radius: 50%; background: var(--teal-pale); margin: 0 auto; display: flex; align-items: center; justify-content: center; }
  .service-icon span { width: 68px; height: 68px; border-radius: 50%; background: var(--teal); display: flex; align-items: center; justify-content: center; }
  .service h3 { font-family: "Raleway", sans-serif; font-weight: 500; font-size: 13px; color: var(--navy); margin-top: 9px; letter-spacing: .3px; }
  .service p { font-size: 7.4px; line-height: 9.2px; margin: 3px auto 0; width: 132px; color: #111; }
  .service .read-more { position: absolute; left: 0; width: 100%; top: 163px; font-size: 7.4px; font-weight: 600; color: var(--orange); text-decoration: none; }

  /* offer */
  .offer { position: absolute; left: 0; top: 542px; width: 100%; height: 220px; background: var(--grey-section); border-top: 1px solid var(--line); border-bottom: 1px solid var(--line); }
  .offer-photo { position: absolute; left: 55px; top: 0; width: 258px; height: 219px;
    background: linear-gradient(180deg, #4e6287 0%, #3c4f73 55%, #d8c3b4 100%); }
  .offer h2 { position: absolute; left: 366px; top: 9px; font-family: "Raleway", sans-serif; font-weight: 500; font-size: 20px; color: var(--navy); }
  .offer ul { position: absolute; left: 369px; top: 35px; list-style: none; }
  .offer li { font-size: 9.2px; height: 15.3px; line-height: 15.3px; color: var(--navy); display: flex; align-items: center; gap: 5px; }

  /* insurance */
  .insurance { position: absolute; left: 0; top: 780px; width: 100%; text-align: center; }
  .insurance h2 { font-family: "Open Sans", sans-serif; font-weight: 700; font-size: 12.5px; color: var(--navy); }
  .insurance p { font-size: 8.2px; margin-top: 4px; }
  .providers { position: absolute; left: 53px; top: 42px; display: flex; gap: 6px; }
  .provider { width: 92px; height: 51px; border: 1px solid var(--line); display: flex; align-items: center; justify-content: center; gap: 4px; font-size: 8.5px; font-weight: 600; color: var(--navy); }
  .provider i { width: 8px; height: 8px; background: var(--navy); display: block; flex: none; }

  /* contact band */
  .call-band { position: absolute; left: 0; top: 892px; width: 100%; height: 51px; background: var(--band-dark); color: #fff; }
  .call-band .band-name { position: absolute; left: 162px; top: 15px; font-family: "Raleway", sans-serif; font-size: 15px; font-weight: 500; }
  .call-band .phone-icon { position: absolute; left: 346px; top: 13px; width: 23px; height: 23px; background: var(--orange); border-radius: 3px; display: flex; align-items: center; justify-content: center; }
  .call-band .phone-number { position: absolute; left: 377px; top: 10px; font-family: "Raleway", sans-serif; font-size: 22px; font-weight: 500; }

  /* footer */
  .site-footer { position: absolute; left: 0; top: 943px; width: 100%; height: 49px; background: var(--footer); color: #cfcfcf; }
  .footer-links { position: absolute; left: 53px; top: 14px; font-size: 7.2px; }
  .footer-links a { color: #cfcfcf; text-decoration: none; }
  .footer-links .sep { margin: 0 6px; }
  .copyright { position: absolute; left: 53px; top: 26px; font-size: 7.2px; color: #e5e5e5; }
  .social { position: absolute; left: 557px; top: 15px; display: flex; gap: 4px; }
  .social span { width: 17px; height: 17px; border-radius: 50%; background: #555; display: block; }
</style>
</head>
<body>
<div class="page">

  <header class="site-header">
    <div class="brand"><span class="brand-dot"></span><span class="brand-name">Maple Ridge Wellness</span></div>
    <nav class="main-nav">
      <a class="active" href="#">Home</a>
      <a class="n-programs" href="#">Programs</a>
      <a class="n-admissions" href="#">Admissions</a>
      <a class="n-about" href="#">About Us</a>
      <a class="n-contact" href="#">Contact Us</a>
    </nav>
  </header>

  <section class="hero">
    <div class="hero-photo" role="img" aria-label="Photo of a smiling female doctor with a stethoscope in a bright clinic"></div>
    <h1 class="hero-title"><span class="line-1">A NEW DAY</span><span class="line-2">IS POSSIBLE</span></h1>
  </section>

  <section class="services">
    <div class="service" style="left:50px">
      <div class="service-icon"><span>
        <svg width="34" height="34" viewBox="0 0 34 34" fill="#fff"><rect x="15.8" y="16" width="2.4" height="14"/><path d="M17 18 C17 9 23 5 31 5 C31 13 26 18 17 18Z"/><path d="M16 20 C16 14 11 11 4 12 C5 18 9 21 16 20Z"/></svg>
      </span></div>
      <h3>HOLISTIC</h3>
      <p>At Maple Ridge Wellness we treat each person not just their addiction. Our homes are in a country setting away from all the distractions of daily life.</p>
      <a class="read-more" href="#">Read More</a>
    </div>
    <div class="service" style="left:206px">
      <div class="service-icon"><span>
        <svg width="36" height="34" viewBox="0 0 36 34"><path d="M18 30 C8 22 3 17 3 11 C3 6 7 3 11 3 C14 3 16.5 5 18 7 C19.5 5 22 3 25 3 C29 3 33 6 33 11 C33 17 28 22 18 30Z" fill="none" stroke="#fff" stroke-width="2.6"/><polyline points="5,17 12,17 15,11 19,23 22,14 24,17 31,17" fill="none" stroke="#fff" stroke-width="2.2"/></svg>
      </span></div>
      <h3>IOP / OP</h3>
      <p>Our intensive outpatient program consists of group therapy, one on one counseling, educational workshops and activities. Clients will typically attend...</p>
      <a class="read-more" href="#">Read More</a>
    </div>
    <div class="service" style="left:350px">
      <div class="service-icon"><span>
        <svg width="36" height="24" viewBox="0 0 36 24" fill="none" stroke="#fff" stroke-width="3"><polyline points="10,4 3,12 10,20"/><polyline points="26,4 33,12 26,20"/><line x1="21" y1="3" x2="15" y2="21"/></svg>
      </span></div>
      <h3>PHP</h3>
      <p>Once the detoxification process is complete, we highly recommend a minimum of 30 days (or longer if needed) stay in one of our community...</p>
      <a class="read-more" href="#">Read More</a>
    </div>
    <div class="service" style="left:499px">
      <div class="service-icon"><span>
        <svg width="38" height="26" viewBox="0 0 38 26" fill="#fff"><polygon points="1,6 8,3 13,14 6,17"/><polygon points="37,6 30,3 25,14 32,17"/><path d="M10 7 L17 5 L22 8 L28 7 L29 14 L20 22 Q18 23 16 21 L9 15Z"/></svg>
      </span></div>
      <h3>STABILIZATION</h3>
      <p>At Maple Ridge Wellness we offer specialized treatment for those struggling to maintain their sobriety due to relapse. It is not unusual for those who have...</p>
      <a class="read-more" href="#">Read More</a>
    </div>
  </section>

  <section class="offer">
    <div class="offer-photo" role="img" aria-label="Photo of a fitness coach in a blue t-shirt holding a clipboard, giving a thumbs up"></div>
    <h2>We Offer</h2>
    <ul>
      <li><svg width="10" height="9" viewBox="0 0 10 9"><polyline points="1,5 4,8 9,1" fill="none" stroke="#22d3c5" stroke-width="2"/></svg>Addiction Treatment Program w/ Housing</li>
      <li><svg width="10" height="9" viewBox="0 0 10 9"><polyline points="1,5 4,8 9,1" fill="none" stroke="#22d3c5" stroke-width="2"/></svg>Intensive Outpatient Treatment Programs</li>
      <li><svg width="10" height="9" viewBox="0 0 10 9"><polyline points="1,5 4,8 9,1" fill="none" stroke="#22d3c5" stroke-width="2"/></svg>Outpatient</li>
      <li><svg width="10" height="9" viewBox="0 0 10 9"><polyline points="1,5 4,8 9,1" fill="none" stroke="#22d3c5" stroke-width="2"/></svg>M.D. on Staff</li>
      <li><svg width="10" height="9" viewBox="0 0 10 9"><polyline points="1,5 4,8 9,1" fill="none" stroke="#22d3c5" stroke-width="2"/></svg>After Care Programs</li>
      <li><svg width="10" height="9" viewBox="0 0 10 9"><polyline points="1,5 4,8 9,1" fill="none" stroke="#22d3c5" stroke-width="2"/></svg>Daily One on One and Group Therapy</li>
      <li><svg width="10" height="9" viewBox="0 0 10 9"><polyline points="1,5 4,8 9,1" fill="none" stroke="#22d3c5" stroke-width="2"/></svg>Family Therapy</li>
      <li><svg width="10" height="9" viewBox="0 0 10 9"><polyline points="1,5 4,8 9,1" fill="none" stroke="#22d3c5" stroke-width="2"/></svg>Life Skills including proper nutrition, &nbsp; exercise &amp; more</li>
      <li><svg width="10" height="9" viewBox="0 0 10 9"><polyline points="1,5 4,8 9,1" fill="none" stroke="#22d3c5" stroke-width="2"/></svg>Weekly massage therapy, yoga and Thai Chi classes</li>
      <li><svg width="10" height="9" viewBox="0 0 10 9"><polyline points="1,5 4,8 9,1" fill="none" stroke="#22d3c5" stroke-width="2"/></svg>Daily activities such as volleyball, &nbsp;private pool etc.</li>
      <li><svg width="10" height="9" viewBox="0 0 10 9"><polyline points="1,5 4,8 9,1" fill="none" stroke="#22d3c5" stroke-width="2"/></svg>Weekly equine therapy and trips to the Beach</li>
    </ul>
  </section>

  <section class="insurance">
    <h2>INSURANCE PROVIDERS</h2>
    <p>We have billed the following insurance providers for our services:</p>
    <div class="providers">
      <div class="provider"><i></i>Crestline Health</div>
      <div class="provider"><i></i>Verano Care</div>
      <div class="provider"><i></i>Harborline</div>
      <div class="provider"><i></i>Altavia</div>
      <div class="provider"><i></i>Unity Medical</div>
      <div class="provider" style="font-size:7.5px"><i></i>State Family Services</div>
    </div>
  </section>

  <section class="call-band">
    <span class="band-name">Maple Ridge Wellness</span>
    <span class="phone-icon"><svg width="13" height="13" viewBox="0 0 24 24" fill="#fff"><path d="M6.6 10.8a15.2 15.2 0 0 0 6.6 6.6l2.2-2.2a1 1 0 0 1 1-.25 11.4 11.4 0 0 0 3.6.57 1 1 0 0 1 1 1V20a1 1 0 0 1-1 1A17 17 0 0 1 3 4a1 1 0 0 1 1-1h3.5a1 1 0 0 1 1 1c0 1.250.2 2.450.57 3.57a1 1 0 0 1-.25 1z"/></svg></span>
    <span class="phone-number">800-555-0142</span>
  </section>

  <footer class="site-footer">
    <div class="footer-links">
      <a href="#">Home</a><span class="sep">|</span><a href="#">Programs</a><span class="sep">|</span><a href="#">Admissions</a><span class="sep">|</span><a href="#">About Us</a><span class="sep">|</span><a href="#">Contact Us</a>
    </div>
    <div class="copyright">Copyright 2014-2015 Maple Ridge Wellness, Inc. All Rights Reserved.</div>
    <div class="social" aria-label="Social links"><span></span><span></span><span></span><span></span></div>
  </footer>

</div>
</body>
</html>
```